Business Card Design Project

Create an impressive business care to use
Updates

My logo is available at http://corvalune.example, or

Industry/Entity Type

Business

Requirements
Must have
• company logo

```html
<!DOCTYPE html>
<html lang="en">
<head>
<meta charset="utf-8">
<title>Corvalune Research Corporation – Business Cards</title>
<link rel="stylesheet" href="https://fonts.googleapis.com/css2?family=Source+Sans+3:wght@400;600&display=swap">
<style>
  :root {
    --backdrop: #6b3216;
    --card-white: #ffffff;
    --card-grey-center: #f7f7f7;
    --card-grey-edge: #c9c9c9;
    --ink-dark: #1f1f1f;
    --ink-grey: #8a8a8a;
    --ink-grey-strong: #6f6f6f;
    --rule: #cfcfcf;
    --accent-orange: #f6a93b;
  }
  html, body {
    margin: 0;
    padding: 0;
    overflow: hidden;
  }
  body {
    width: 1200px;
    height: 789px;
    background: var(--backdrop);
    font-family: "Source Sans 3", Arial, sans-serif;
    position: relative;
  }
  .card {
    position: absolute;
    width: 530px;
    height: 300px;
    background: var(--card-white);
    box-sizing: border-box;
    box-shadow: 0 4px 12px rgba(0,0,0,0.35);
    overflow: hidden;
  }
  .card--details { left: 60px;  top: 55px; }
  .card--logo    { left: 610px; top: 55px; }
  .card--grey    { left: 60px;  top: 430px;
    background: radial-gradient(ellipse at 50% 45%, var(--card-grey-center) 0%, var(--card-grey-edge) 100%); }
  .card--symbol  { left: 610px; top: 430px; }

  .wordmark {
    display: flex;
    align-items: center;
    gap: 10px;
    color: var(--ink-dark);
    font-weight: 600;
    letter-spacing: 0.08em;
    text-transform: uppercase;
    white-space: nowrap;
  }
  .wordmark__dot {
    width: 18px;
    height: 18px;
    border-radius: 50%;
    background: var(--accent-orange);
    flex: none;
  }
  .wordmark--large { font-size: 20px; }
  .wordmark--small { font-size: 16px; }
  .wordmark--small .wordmark__dot { width: 15px; height: 15px; }

  .centered-mark {
    position: absolute;
    left: 30px; right: 30px;
    top: 124px;
    display: flex;
    justify-content: center;
  }
  .card-url {
    position: absolute;
    left: 0; right: 0;
    bottom: 16px;
    text-align: center;
    font-size: 13px;
    color: var(--ink-grey);
  }

  /* details card */
  .details-head {
    position: absolute;
    top: 28px; left: 0; right: 0;
    display: flex;
    flex-direction: column;
    align-items: center;
  }
  .person {
    margin-top: 18px;
    text-align: center;
    color: var(--ink-grey-strong);
    line-height: 1.2;
  }
  .person__name { font-weight: 600; font-size: 15px; }
  .person__native, .person__role { font-size: 14px; }
  .details-rule {
    position: absolute;
    left: 24px; right: 24px;
    top: 150px;
    border-top: 1px solid var(--rule);
  }
  .office {
    position: absolute;
    top: 162px;
    font-size: 12.5px;
    line-height: 1.35;
    color: var(--ink-grey);
    font-style: normal;
  }
  .office--us    { left: 28px; }
  .office--china { left: 276px; }
  .office__label { font-weight: 600; color: var(--ink-grey-strong); }

  .symbol-disc {
    position: absolute;
    left: 50%;
    top: 100px;
    width: 84px;
    height: 84px;
    margin-left: -42px;
    border-radius: 50%;
    background: var(--accent-orange);
  }
</style>
</head>
<body>

  <section class="card card--details" aria-label="Business card front with contact details">
    <div class="details-head">
      <div class="wordmark wordmark--small"><span class="wordmark__dot"></span>Corvalune Research Corporation</div>
      <div class="person">
        <div class="person__name">Martin Lei Soong, PhD</div>
        <div class="person__native">宋磊 博士</div>
        <div class="person__role">CEO</div>
      </div>
    </div>
    <div class="details-rule"></div>
    <address class="office office--us">
      <div class="office__label">U.S.</div>
      4820 Harbor Crest Ave, Suite 210<br>
      Lakemont, CA 90000<br>
      Email: msoong@corvalune.example<br>
      Cell: 555-014-2297<br>
      http://www.corvalune.example
    </address>
    <address class="office office--china">
      <div class="office__label">China</div>
      880, NO.12 Linhe Road, Xiyuan<br>
      District, Nanshan, China 100999<br>
      南山市西苑区临河路12号锦川国际<br>
      http://www.harlowen.example
    </address>
  </section>

  <section class="card card--logo" aria-label="Business card back with company name">
    <div class="centered-mark">
      <div class="wordmark wordmark--large"><span class="wordmark__dot"></span>Corvalune Research Corporation</div>
    </div>
    <div class="card-url">www.corvalune.example</div>
  </section>

  <section class="card card--grey" aria-label="Grey business card with company name">
    <div class="centered-mark">
      <div class="wordmark wordmark--large"><span class="wordmark__dot"></span>Corvalune Research Corporation</div>
    </div>
    <div class="card-url">www.corvalune.example</div>
  </section>

  <section class="card card--symbol" aria-label="White business card with company mark">
    <div class="symbol-disc"></div>
    <div class="card-url">www.corvalune.example</div>
  </section>

</body>
</html>
```